Simple AD for Digital Publication

Total Size 5" x 5", may include boarder or not
Image Provided; crop or use as background
Incorporate Logo and text as provided

Target Market(s)

Sound Contractors / Integrators

Industry/Entity Type

Audio Video Lighting

Requirements
Must have
• Bold Look that reflects our brand. see website: tovermundic.com - cohesive text and style

```html
<!DOCTYPE html>
<html lang="en">
<head>
<meta charset="utf-8">
<title>Tovermundic Co – Flush Stage Pockets and Panels</title>
<link rel="stylesheet" href="https://fonts.googleapis.com/css2?family=Raleway:wght@400;500;700;800&display=swap">
<style>
  :root {
    --brand-red: #a91e23;
    --ink-dark: #3a3a3c;
    --ink-black: #1c1c1c;
    --paper: #ffffff;
    --photo-deep: #1f2a1e;
    --photo-green: #2f4a2c;
    --photo-warm: #6b5a55;
    --photo-floor: #857c88;
    --photo-floor-light: #9a929c;
  }
  * { box-sizing: border-box; margin: 0; padding: 0; }
  html, body {
    width: 1200px;
    height: 1200px;
    overflow: hidden;
    background: var(--paper);
  }
  .ad {
    position: relative;
    width: 1200px;
    height: 1200px;
    background: var(--brand-red);
    font-family: "Raleway", sans-serif;
  }
  .ad__sheet {
    position: absolute;
    left: 6px;
    top: 30px;
    width: 1188px;
    height: 1138px;
    background: var(--paper);
  }
  .brand {
    position: absolute;
    left: 640px;
    top: 70px;
    display: flex;
    align-items: center;
    gap: 16px;
  }
  .brand__mark {
    width: 34px;
    height: 34px;
    background: var(--brand-red);
  }
  .brand__name {
    font-weight: 800;
    font-size: 46px;
    letter-spacing: -0.5px;
    color: var(--ink-dark);
    line-height: 1;
  }
  .brand__tagline {
    position: absolute;
    left: 690px;
    top: 120px;
    font-weight: 700;
    font-size: 23px;
    color: var(--ink-dark);
  }
  .hero {
    position: absolute;
    left: 6px;
    top: 190px;
    width: 1188px;
    height: 698px;
    background:
      radial-gradient(ellipse at 60% 70%, rgba(30,30,30,0.55) 0%, rgba(30,30,30,0) 45%),
      linear-gradient(180deg,
        var(--photo-deep) 0%,
        var(--photo-green) 22%,
        var(--photo-green) 34%,
        var(--photo-warm) 50%,
        var(--photo-floor) 70%,
        var(--photo-floor-light) 100%);
  }
  .hero__copy {
    position: absolute;
    left: 56px;
    top: 395px;
    color: var(--paper);
  }
  .hero__title {
    font-weight: 500;
    font-size: 51px;
    line-height: 68px;
  }
  .hero__lede {
    margin-top: 4px;
    font-weight: 400;
    font-size: 38px;
    line-height: 66px;
  }
  .pitch {
    position: absolute;
    left: 62px;
    top: 946px;
    font-weight: 500;
    font-size: 53px;
    line-height: 72px;
    color: var(--brand-red);
  }
  .dealer {
    position: absolute;
    left: 870px;
    top: 936px;
    width: 270px;
    text-align: center;
    text-decoration: none;
    color: var(--ink-black);
  }
  .dealer__label {
    display: block;
    font-weight: 500;
    font-size: 27px;
    text-align: right;
  }
  .dealer__icon {
    display: block;
    margin: 10px 0 0 84px;
  }
  .dealer__hint {
    display: block;
    margin-top: 2px;
    text-align: right;
    font-size: 21px;
    color: var(--ink-dark);
  }
</style>
</head>
<body>
  <main class="ad">
    <div class="ad__sheet"></div>

    <header>
      <div class="brand">
        <span class="brand__mark"></span>
        <span class="brand__name">TOVERMUNDIC CO</span>
      </div>
      <p class="brand__tagline">Stage Pocket Systems Connectivity</p>
    </header>

    <section class="hero" role="img" aria-label="Photo of a black flush stage pocket set into a wooden stage floor with cables running out of it, evergreen garland with warm string lights behind">
      <div class="hero__copy">
        <h1 class="hero__title">Flush Stage<br>Pockets and Panels.</h1>
        <p class="hero__lede">Our Products are Smart, Always in Stock,<br>Easy to Install, and Simple to Use.</p>
      </div>
    </section>

    <p class="pitch">Protect and Conceal High<br>and Low Voltage Connectivity</p>

    <a class="dealer" href="#dealer">
      <span class="dealer__label">Become a Dealer</span>
      <svg class="dealer__icon" width="120" height="100" viewBox="0 0 120 100" aria-hidden="true">
        <rect x="28" y="10" width="70" height="70" fill="#4a4a4c"/>
        <path d="M78 50 L78 92 L88 82 L96 98 L103 95 L95 79 L109 79 Z" fill="var(--ink-black)" stroke="#ffffff" stroke-width="3" stroke-linejoin="round"/>
      </svg>
      <span class="dealer__hint">(click here)</span>
    </a>
  </main>
</body>
</html>
```